Corporate Notepads

We currently have a basic notepad with our logo and icon at the top along with contact information at the bottom. We want to come up with something more creative and jazz it up a bit. We are looking for unique ideas to make the notepads look nice and corporate possibly with watermarked look. We will take any ideas and choose the one that works best for the look. We have a website where you can get ideas about our company. Attached is the current simple notepad design we have right now.

```html
<!DOCTYPE html>
<html lang="en">
<head>
<meta charset="utf-8">
<title>Hartwell Construction Notepad</title>
<link href="https://fonts.googleapis.com/css2?family=Oswald:wght@500;600&display=swap" rel="stylesheet">
<style>
  :root {
    --backdrop: #ece2d4;
    --paper: #ffffff;
    --brand-blue: #223f8c;
    --ink-black: #111111;
    --rule-grey: #8a8a8a;
    --mark-tint: #eef0f4;
    --footer-text: #ffffff;
  }
  * { margin: 0; padding: 0; box-sizing: border-box; }
  html, body {
    width: 1200px;
    height: 673px;
    overflow: hidden;
    background: var(--backdrop);
    font-family: "Oswald", "Arial Narrow", sans-serif;
  }
  .canvas {
    position: relative;
    width: 1200px;
    height: 673px;
  }
  .notepad {
    position: absolute;
    left: 373px;
    top: 16px;
    width: 453px;
    height: 640px;
    background: var(--paper);
    overflow: hidden;
    box-shadow: 0 2px 10px rgba(0,0,0,0.12);
  }
  .header-wave {
    position: absolute;
    left: 0;
    top: 0;
    width: 453px;
    height: 132px;
  }
  .brand {
    position: absolute;
    right: 62px;
    top: 44px;
    display: flex;
    align-items: center;
    gap: 10px;
    color: var(--brand-blue);
    font-weight: 600;
  }
  .brand-square {
    width: 50px;
    height: 50px;
    background: var(--brand-blue);
  }
  .brand-name {
    display: flex;
    flex-direction: column;
    align-items: center;
    line-height: 1;
  }
  .brand-name .primary {
    font-size: 40px;
    letter-spacing: 0.5px;
  }
  .brand-name .secondary {
    font-size: 16px;
    letter-spacing: 1px;
    margin-top: 2px;
  }
  .watermark-block {
    position: absolute;
    left: 92px;
    top: 180px;
    width: 270px;
    height: 270px;
    background: var(--mark-tint);
  }
  .ruled-lines {
    position: absolute;
    left: 0;
    top: 130px;
    width: 100%;
    height: 458px;
    background-image: repeating-linear-gradient(
      to bottom,
      transparent 0,
      transparent 21.8px,
      var(--rule-grey) 21.8px,
      var(--rule-grey) 22.8px
    );
  }
  .footer-band {
    position: absolute;
    left: 0;
    bottom: 0;
    width: 100%;
    height: 43px;
    background: var(--ink-black);
    color: var(--footer-text);
    display: flex;
    align-items: center;
    padding: 0 18px;
    font-size: 11.5px;
    font-weight: 500;
    letter-spacing: 0.2px;
    white-space: nowrap;
  }
  .footer-band .service { margin-right: 14px; }
  .footer-band .service.spaced { margin-right: 24px; }
  .footer-band .bullet { margin-right: 6px; }
  .footer-band .web {
    display: flex;
    align-items: center;
    gap: 5px;
    margin-right: 14px;
  }
  .footer-band .web-square {
    width: 8px;
    height: 8px;
    border: 1.3px solid var(--footer-text);
  }
</style>
</head>
<body>
  <main class="canvas">
    <article class="notepad">
      <svg class="header-wave" viewBox="0 0 516 150" preserveAspectRatio="none" aria-hidden="true">
        <path d="M0 0 H516 V74 C440 22 340 -6 262 14 C180 36 120 100 0 106 Z" fill="var(--brand-blue)"/>
        <path d="M0 106 C120 100 180 36 262 14 C210 20 160 62 110 100 C80 120 40 128 0 128 Z" fill="var(--ink-black)"/>
      </svg>

      <div class="brand">
        <span class="brand-square"></span>
        <span class="brand-name">
          <span class="primary">HARTWELL</span>
          <span class="secondary">— CONSTRUCTION —</span>
        </span>
      </div>

      <div class="watermark-block"></div>
      <div class="ruled-lines"></div>

      <footer class="footer-band">
        <span class="service spaced">CIVIL</span>
        <span class="bullet">•</span><span class="service spaced">INDUSTRIAL</span>
        <span class="bullet">•</span><span class="service spaced">COMERCIAL</span>
        <span class="web"><span class="web-square"></span>HartwellBuilds.com</span>
        <span class="bullet">•</span><span class="phone">555.014.2290</span>
      </footer>
    </article>
  </main>
</body>
</html>
```